A compelling brochure for a children's charity to encourage donations

We are looking for a 4-page A-4 booklet (1 x A3 page folded in half). the Lantern Harbour Foundation is a non-profit organisation that aims to reduce the incidence and impact of children's critical injury in Australia. The brochure will give people who are new to the charity, an overview of who we are, what we do, why we do it and how they can help. You can reference our website www.lanternharbourkids.org.au for colours and styles. The final design should encourage people to make a donation by being positive and powerful.
Use the text in the uploaded files.

```html
<!DOCTYPE html>
<html lang="en">
<head>
<meta charset="utf-8">
<title>Vital Support – Lantern Harbour Foundation</title>
<link rel="stylesheet" href="https://fonts.googleapis.com/css2?family=Montserrat:wght@300;400;600;700&display=swap">
<style>
  :root {
    --magenta: #b8106b;
    --text-grey: #555559;
    --heading-grey: #4a4a4e;
    --donate-orange: #f6a623;
    --white: #ffffff;
    --photo-top: #8f8a78;
    --photo-bottom: #c9b7a4;
  }
  * { margin: 0; padding: 0; box-sizing: border-box; }
  html, body { width: 849px; height: 1200px; overflow: hidden; background: var(--white); }
  body { font-family: "Montserrat", Arial, sans-serif; color: var(--text-grey); }
  .page { position: relative; width: 849px; height: 1200px; overflow: hidden; }

  .hero {
    position: absolute; left: 0; top: 0; width: 849px; height: 216px;
    background: linear-gradient(100deg, var(--photo-top) 0%, var(--photo-bottom) 45%, #b79a86 70%, var(--photo-top) 100%);
  }
  .hero-title {
    position: absolute; right: 44px; top: 16px;
    font-size: 33px; font-weight: 600; color: rgba(255,255,255,0.7); letter-spacing: 0.3px;
  }
  .hero-rule { position: absolute; left: 0; top: 216px; width: 849px; height: 8px; background: var(--magenta); }

  .content { position: absolute; left: 62px; width: 730px; }
  .lead { top: 246px; font-size: 26px; line-height: 32px; font-weight: 300; color: var(--heading-grey); }
  .lead strong { font-weight: 600; font-size: 23px; }

  .section-title { position: absolute; left: 62px; font-size: 22px; font-weight: 700; color: var(--magenta); }
  .body-text { font-size: 15px; line-height: 21.5px; font-weight: 400; }
  .body-text strong { font-weight: 700; color: #3f3f43; }

  .bullets { list-style: none; }
  .bullets li { position: relative; padding-left: 27px; }
  .bullets li::before {
    content: ""; position: absolute; left: 0; top: 6px; width: 9px; height: 9px; background: var(--magenta);
  }

  .footer { position: absolute; left: 0; top: 1038px; width: 849px; height: 162px; background: var(--magenta); }
  .footer-name {
    position: absolute; left: 65px; top: 30px;
    font-size: 28px; line-height: 30px; font-weight: 400; color: var(--white);
  }
  .footer-contact { position: absolute; left: 65px; top: 103px; font-size: 13px; line-height: 18px; color: var(--white); }
  .footer-contact b { font-weight: 700; }
  .donate-button {
    position: absolute; left: 600px; top: 36px; width: 200px; height: 70px;
    background: var(--donate-orange); border: 3px solid var(--white); border-radius: 10px; text-align: center;
  }
  .donate-label { display: block; margin-top: 4px; font-size: 33px; line-height: 36px; font-weight: 700; color: var(--magenta); }
  .donate-tagline { display: block; font-size: 15px; font-weight: 700; color: var(--white); }
  .footer-web {
    position: absolute; right: 49px; top: 119px;
    font-size: 17px; font-weight: 700; color: var(--donate-orange); letter-spacing: 0.4px;
  }
</style>
</head>
<body>
<main class="page">
  <div class="hero" role="img" aria-label="Photograph of three smiling teenage girls hugging outdoors"></div>
  <div class="hero-title">Vital Support</div>
  <div class="hero-rule"></div>

  <p class="content lead"><strong>Ultimately we will advocate for systemic change</strong><br>where appropriate in order to reduce the incidence and impact of these tragic accidents.</p>

  <h2 class="section-title" style="top:341px">The Paediatric Critical Injury Research Program</h2>
  <ul class="content bullets body-text" style="top:376px">
    <li style="margin-bottom:13px">Developed and led by Associate Professor Helen Marsh of the Coastal University, Harbourside Nursing School, the 6-year $960,000 program will: <strong>Quantify exactly how and why many children are hospitalised in Australia as a result of severe injury.</strong></li>
    <li style="margin-bottom:13px">Investigate whether ambulance protocols should be mandated to ensure that children are transported directly to a paediatric trauma centre.</li>
    <li>Provide <strong>definitive answers regarding unmet needs</strong> in an Australia-wide, Australian first survey of parents of severely injured children. The program is currently on schedule and on budget.</li>
  </ul>

  <h2 class="section-title" style="top:583px">Informed Interventions</h2>
  <p class="content body-text" style="top:627px">Evidence gathered during the research program will inform interventions to be piloted by the Lantern Harbour Foundation. Prioritised interventions will <strong>focus on family support. Piloted interventions may include:</strong></p>
  <ul class="content bullets body-text" style="top:694px">
    <li style="margin-bottom:6px">Appointment of in-hospital Family Support Coordinator service to assess<br>and support at-risk families</li>
    <li style="margin-bottom:6px">Development of a resilience tool-kit for parents</li>
    <li>A 24-hour help-line for parents and families of critically injured children</li>
  </ul>

  <h2 class="section-title" style="top:802px">Measuring Effectiveness</h2>
  <p class="content body-text" style="top:834px">The effectiveness of interventions will be measured against the data gathered during the Paediatric Critical Injury Research Program.</p>

  <h2 class="section-title" style="top:886px">Advocacy</h2>
  <p class="content body-text" style="top:919px">Advocating improved care for thousands of Australian families, the most effective interventions and services identified will be included in recommendations for health policy change to Federal and State Health Departments. The Lantern Harbour Foundation’s ultimate objective is reducing the incidence and impact of children’s critical injury in Australia.</p>

  <footer class="footer">
    <div class="footer-name">Lantern<br>Harbour</div>
    <div class="footer-contact">
      <div><b>Email:</b> enquiry@lanternharbourkids.org.au</div>
      <div><b>Phone:</b> 02 5550 1234</div>
    </div>
    <div class="donate-button">
      <span class="donate-label">DONATE</span>
      <span class="donate-tagline">Help us Help them!</span>
    </div>
    <div class="footer-web">www.lanternharbourkids.org.au</div>
  </footer>
</main>
</body>
</html>
```